Real Estate Webpage Design

We have an existing website: brindlewoodhomes.com.au
We focus customised service mainly on Property Management and second-hand property sales.
We are not entirely happy about the current design and layout can stay roughly the same as the back end coding is linked to a CRM system.
We would like to see the design are more reachable to our clients and appearing.
Please check our Website Design Draft for more details.

Industry/Entity Type

Real estate Agency

Number of Pages Required

5+ page

Font styles to use
Sans Serif

Colors

Designer to choose colors to be used in the design.

```html
<!DOCTYPE html>
<html lang="en">
<head>
<meta charset="utf-8">
<title>Brindlewood Homes – Tenant</title>
<link href="https://fonts.googleapis.com/css2?family=Poppins:wght@400;500;600&family=Roboto:wght@400;500;700&display=swap" rel="stylesheet">
<style>
:root{
  --navy:#0f2d4a;
  --yellow:#fbc33b;
  --orange:#f5a800;
  --text:#333;
  --muted:#8a8a8a;
  --cream:#fffaec;
  --light:#f5f5f5;
  --white:#fff;
}
*{box-sizing:border-box;margin:0;padding:0}
html,body{width:1200px;height:3387px;overflow:hidden}
body{position:relative;font-family:"Poppins",sans-serif;color:var(--text);background:var(--white);font-size:13px}
.abs{position:absolute}
h1,h2,h3{font-family:"Roboto",sans-serif}

/* header */
.site-header{top:0;left:0;width:1200px;height:60px;background:var(--white)}
.logo-box{left:59px;top:0;width:225px;height:74px;background:var(--white);display:flex;align-items:center;padding-left:20px;gap:10px;z-index:2}
.logo-dot{width:34px;height:34px;background:var(--orange);border-radius:4px}
.logo-name{font-family:"Poppins",sans-serif;font-weight:600;color:var(--orange);font-size:22px;line-height:1}
.main-nav{left:324px;top:23px;display:flex;gap:24px;font-size:13px;color:#222;white-space:nowrap}
.main-nav .active{color:var(--orange);border-bottom:2px solid var(--orange);padding-bottom:13px}
.btn-add{left:1012px;top:18px;width:128px;height:34px;background:var(--orange);color:#fff;font-size:13.5px;display:flex;align-items:center;justify-content:center;border-left:3px solid #d48f00;white-space:nowrap}

/* hero */
.hero{left:0;top:60px;width:1200px;height:352px;background:linear-gradient(180deg,#6d8aa0 0%,#3d4d3a 55%,#2c3826 100%)}
.hero-title{left:62px;top:193px;font-size:39px;font-weight:700;color:var(--orange);font-family:"Roboto",sans-serif}
.hero-sub{left:62px;top:252px;font-size:13px;color:#fff;font-family:"Roboto",sans-serif}

/* search */
.search{left:59px;top:463px;width:1082px;height:55px;background:#fff;box-shadow:0 2px 12px rgba(0,0,0,.08);display:flex;align-items:center}
.search-type{width:108px;height:100%;border-right:2px solid #e4e4e4;display:flex;align-items:center;justify-content:space-between;padding:0 12px 0 14px;font-size:14px}
.caret{width:0;height:0;border-left:6px solid transparent;border-right:6px solid transparent;border-top:7px solid #222}
.search-input{flex:1;padding-left:16px;color:#666;font-size:14px}
.search-btn{width:44px;height:46px;background:var(--orange);margin-right:5px;display:flex;align-items:center;justify-content:center}
.more-options{left:1003px;top:536px;font-size:12px;color:var(--orange)}

/* listing cards */
.card{top:600px;width:518px;height:501px;background:#fff;box-shadow:0 2px 14px rgba(0,0,0,.09)}
.card-photo{position:absolute;left:15px;top:15px;width:492px;height:286px}
.card-tag{position:absolute;left:31px;top:319px;font-size:12px;color:var(--orange)}
.card-suburb{position:absolute;left:31px;top:344px;font-size:17px;color:#222}
.card-addr{position:absolute;left:31px;top:372px;font-size:13px;color:#222;display:flex;gap:6px;align-items:center}
.card-feat{position:absolute;left:31px;top:404px;display:flex;gap:16px;font-size:13px;align-items:center}
.card-feat span{display:flex;gap:6px;align-items:center}
.card-foot{position:absolute;left:0;top:449px;width:518px;height:52px;border-top:2px solid #d9d9d9;display:flex;align-items:center;padding:0 20px;justify-content:space-between}
.agent{display:flex;align-items:center;gap:10px;font-size:13px}
.avatar{width:30px;height:30px;background:#9aa3ab}
.card-actions{display:flex;gap:9px}

/* maintenance */
.maint{left:0;top:1183px;width:1200px;height:415px;background:var(--light)}
.maint-bar{left:60px;top:1237px;width:58px;height:286px;background:var(--navy)}
.maint-photo{left:94px;top:1265px;width:337px;height:248px;background:linear-gradient(135deg,#fbc33b,#f6b522)}
.maint-title{left:503px;top:1229px;font-size:35px;font-weight:700;color:var(--navy)}
.maint-text{left:503px;top:1282px;width:516px;font-size:13px;line-height:22.5px;color:var(--muted);font-family:"Roboto",sans-serif}
.maint-text p+p{margin-top:4px}
.btn-portal{left:503px;top:1494px;width:112px;height:35px;background:var(--orange);color:#fff;font-size:13px;display:flex;align-items:center;justify-content:center;border-left:3px solid #c98b00}

/* urgent */
.urgent{left:0;top:1598px;width:1200px;height:493px;background:var(--navy);color:#fff}
.urgent h2{position:absolute;left:0;width:1200px;text-align:center;top:52px;font-size:35px;font-weight:700}
.urgent-sub{position:absolute;left:300px;width:600px;top:103px;text-align:center;font-size:13px;line-height:22.5px;font-family:"Roboto",sans-serif}
.u-item{position:absolute;font-size:13px;line-height:22.5px;display:flex;gap:24px;font-family:"Roboto",sans-serif;width:440px}
.u-item svg{flex:none;margin-top:4px}

/* emergency */
.section-title{position:absolute;left:0;width:1200px;text-align:center;font-size:35px;font-weight:700;color:var(--navy)}
.section-sub{position:absolute;left:300px;width:600px;text-align:center;font-size:13px;line-height:22.5px;color:var(--muted);font-family:"Roboto",sans-serif}
.filter{left:537px;top:2299px;width:127px;height:35px;border:1px solid var(--orange);display:flex;align-items:center;justify-content:space-between;padding:0 12px 0 14px;font-size:13px}
.trade{top:2370px;width:341px;height:265px;background:var(--cream);box-shadow:0 2px 12px rgba(0,0,0,.05);text-align:center}
.trade h3{margin-top:28px;font-size:35px;line-height:40px;font-weight:700;color:var(--navy)}
.trade-desc{margin-top:42px;font-size:16px;color:var(--orange)}
.trade-phone{margin:20px auto 0;width:112px;height:35px;background:var(--orange);color:#fff;font-size:13px;font-weight:600;display:flex;align-items:center;justify-content:center;border-left:3px solid #c98b00;font-family:"Roboto",sans-serif}

/* tenancy */
.tenancy{left:0;top:2718px;width:1200px;height:335px;background:var(--cream)}

/* footer */
.footer-logo{left:61px;top:3110px;display:flex;align-items:center;gap:10px}
.footer-about{left:61px;top:3164px;width:200px;font-size:13px;line-height:22.5px}
.f-head{font-size:13px;color:var(--orange)}
.f-links{left:336px;top:3118px;font-size:12.5px;line-height:29.5px}
.f-contact{left:613px;top:3090px;font-size:13px}
.f-row{display:flex;gap:14px;margin-top:12px;line-height:20px}
.f-social{left:890px;top:3090px}
.soc{display:flex;gap:16px;margin-top:18px}
.soc span{width:38px;height:38px;border-radius:50%;border:2px solid var(--orange);display:block}
.soc span.fill{background:var(--orange)}
.bottom{left:0;top:3345px;width:1200px;height:42px;border-top:1px solid #ddd;font-size:12px;display:flex;align-items:center;justify-content:space-between;padding:0 60px 0 61px}
.bottom nav{display:flex;gap:27px}
</style>
</head>
<body>

<header class="abs site-header">
  <div class="abs logo-box"><span class="logo-dot"></span><span class="logo-name">Brindlewood</span></div>
  <nav class="abs main-nav">
    <span>Home</span><span>About Us</span><span>Landload</span><span class="active">Tenant</span><span>Make a Switch</span><span>Property Sales</span><span>Appraisal now</span>
  </nav>
  <div class="abs btn-add">Add Properties</div>
</header>

<section>
  <div class="abs hero" role="img" aria-label="Modern two-storey house with pool and trees"></div>
  <h1 class="abs hero-title">Landlord</h1>
  <p class="abs hero-sub">Your local real estate property group</p>
</section>

<form class="abs search">
  <div class="search-type">Rent <span class="caret"></span></div>
  <div class="search-input">Search by Suburb, Postcode or keyword</div>
  <div class="search-btn"><svg width="20" height="20" viewBox="0 0 20 20" fill="none" stroke="#fff" stroke-width="2"><circle cx="8.5" cy="8.5" r="6"/><path d="M13 13l5 5"/></svg></div>
</form>
<div class="abs more-options">+&nbsp;&nbsp; View More Options</div>

<article class="abs card" style="left:59px">
  <div class="card-photo" role="img" aria-label="Rooftop pool beside apartment tower" style="background:linear-gradient(135deg,#7e8a90 0%,#a9c4dc 45%,#2f5fa8 100%)"></div>
  <div class="card-tag">For Lease</div>
  <div class="card-suburb">Harwood</div>
  <div class="card-addr"><svg width="13" height="17" viewBox="0 0 13 17" fill="none" stroke="#f5a800" stroke-width="1.3"><path d="M6.5 16S1 9.5 1 6a5.5 5.5 0 0111 0c0 3.5-5.5 10-5.5 10z"/><circle cx="6.5" cy="6" r="2"/></svg>18 Kestrel Lane Harwood</div>
  <div class="card-feat">
    <span><svg width="22" height="14" fill="none" stroke="#f5a800" stroke-width="1.3"><rect x="1" y="5" width="20" height="6"/><rect x="3" y="1" width="16" height="4"/></svg>3</span>
    <span><svg width="22" height="14" fill="none" stroke="#f5a800" stroke-width="1.3"><path d="M1 7h20v3a3 3 0 01-3 3H4a3 3 0 01-3-3z"/><path d="M4 7V2h3"/></svg>2</span>
    <span><svg width="26" height="14" fill="none" stroke="#f5a800" stroke-width="1.3"><path d="M1 10V7l4-4h12l6 4v3z"/><circle cx="6" cy="11" r="2"/><circle cx="19" cy="11" r="2"/></svg>2</span>
  </div>
  <div class="card-foot">
    <div class="agent"><span class="avatar"></span>Mara Quill</div>
    <div class="card-actions">
      <svg width="18" height="18" fill="none" stroke="#444" stroke-width="1.3"><circle cx="9" cy="9" r="7.5"/><path d="M9 4v5l3 2"/></svg>
      <svg width="17" height="17" fill="none" stroke="#444" stroke-width="1.3"><path d="M1 6V1h5M11 1h5v5M16 11v5h-5M6 16H1v-5M1 1l5 5M16 1l-5 5M16 16l-5-5M1 16l5-5"/></svg>
      <svg width="20" height="16" fill="none" stroke="#444" stroke-width="1.3"><rect x="1" y="1" width="18" height="14"/><path d="M1 1l9 7 9-7"/></svg>
    </div>
  </div>
</article>

<article class="abs card" style="left:623px">
  <div class="card-photo" role="img" aria-label="Furnished living room with balcony" style="background:linear-gradient(135deg,#8d8d8a 0%,#c9c8c2 45%,#6a4a30 100%)"></div>
  <div class="card-tag">For Lease</div>
  <div class="card-suburb">Elmsdale</div>
  <div class="card-addr"><svg width="13" height="17" viewBox="0 0 13 17" fill="none" stroke="#f5a800" stroke-width="1.3"><path d="M6.5 16S1 9.5 1 6a5.5 5.5 0 0111 0c0 3.5-5.5 10-5.5 10z"/><circle cx="6.5" cy="6" r="2"/></svg>7 Ferncroft Road Elmsdale</div>
  <div class="card-feat">
    <span><svg width="22" height="14" fill="none" stroke="#f5a800" stroke-width="1.3"><rect x="1" y="5" width="20" height="6"/><rect x="3" y="1" width="16" height="4"/></svg>2</span>
    <span><svg width="22" height="14" fill="none" stroke="#f5a800" stroke-width="1.3"><path d="M1 7h20v3a3 3 0 01-3 3H4a3 3 0 01-3-3z"/><path d="M4 7V2h3"/></svg>2</span>
    <span><svg width="26" height="14" fill="none" stroke="#f5a800" stroke-width="1.3"><path d="M1 10V7l4-4h12l6 4v3z"/><circle cx="6" cy="11" r="2"/><circle cx="19" cy="11" r="2"/></svg>1</span>
  </div>
  <div class="card-foot">
    <div class="agent"><span class="avatar"></span>Mara Quill</div>
    <div class="card-actions">
      <svg width="18" height="18" fill="none" stroke="#444" stroke-width="1.3"><circle cx="9" cy="9" r="7.5"/><path d="M9 4v5l3 2"/></svg>
      <svg width="17" height="17" fill="none" stroke="#444" stroke-width="1.3"><path d="M1 6V1h5M11 1h5v5M16 11v5h-5M6 16H1v-5M1 1l5 5M16 1l-5 5M16 16l-5-5M1 16l5-5"/></svg>
      <svg width="20" height="16" fill="none" stroke="#444" stroke-width="1.3"><rect x="1" y="1" width="18" height="14"/><path d="M1 1l9 7 9-7"/></svg>
    </div>
  </div>
</article>

<section>
  <div class="abs maint"></div>
  <div class="abs maint-bar"></div>
  <div class="abs maint-photo" role="img" aria-label="Tradesperson holding a wrench and toolbox"></div>
  <h2 class="abs maint-title">Maintenance request</h2>
  <div class="abs maint-text">
    <p>Lorem Ipsum is simply dummy text of the printing and typesetting industry. Lorem Ipsum has been the industry's standard dummy text ever since the 1500s, when an unknown printer took a galley of type and scrambled it to make a type specimen book. It has survived not only five centuries, but also the leap into electronic typesetting, remaining essentially unchanged.</p>
    <p>Lorem Ipsum is simply dummy text of the printing and typesetting industry. Lorem Ipsum has been the industry's standard dummy text ever since the 1500s, when an unknown printer took a galley.</p>
  </div>
  <div class="abs btn-portal">Tenant Portal</div>
</section>

<section class="abs urgent">
  <h2>What is “Urgent maintenance”</h2>
  <p class="urgent-sub">Lorem Ipsum is simply dummy text of the printing and typesetting industry. Lorem Ipsum has been the industry's standard dummy text.</p>
  <div class="u-item" style="left:119px;top:177px"><svg width="16" height="16"><path d="M1 1l14 7-14 7 4-7z" fill="#fbc33b"/></svg><span>Lorem Ipsum is simply dummy text of the printing and typesetting industry.</span></div>
  <div class="u-item" style="left:119px;top:231px"><svg width="16" height="16"><path d="M1 1l14 7-14 7 4-7z" fill="#fbc33b"/></svg><span>Lorem Ipsum is simply dummy text.</span></div>
  <div class="u-item" style="left:119px;top:272px"><svg width="16" height="16"><path d="M1 1l14 7-14 7 4-7z" fill="#fbc33b"/></svg><span>Lorem Ipsum is simply dummy text.</span></div>
  <div class="u-item" style="left:119px;top:308px"><svg width="16" height="16"><path d="M1 1l14 7-14 7 4-7z" fill="#fbc33b"/></svg><span>Lorem Ipsum is simply dummy text.</span></div>
  <div class="u-item" style="left:119px;top:349px"><svg width="16" height="16"><path d="M1 1l14 7-14 7 4-7z" fill="#fbc33b"/></svg><span>Lorem Ipsum is simply dummy text.</span></div>
  <div class="u-item" style="left:119px;top:385px"><svg width="16" height="16"><path d="M1 1l14 7-14 7 4-7z" fill="#fbc33b"/></svg><span>Lorem Ipsum is simply dummy text.</span></div>
  <div class="u-item" style="left:119px;top:425px"><svg width="16" height="16"><path d="M1 1l14 7-14 7 4-7z" fill="#fbc33b"/></svg><span>Lorem Ipsum is simply dummy text.</span></div>
  <div class="u-item" style="left:624px;top:177px"><svg width="16" height="16"><path d="M1 1l14 7-14 7 4-7z" fill="#fbc33b"/></svg><span>Lorem Ipsum is simply dummy text of the printing and typesetting industry.</span></div>
  <div class="u-item" style="left:624px;top:231px"><svg width="16" height="16"><path d="M1 1l14 7-14 7 4-7z" fill="#fbc33b"/></svg><span style="margin-left:8px">Lorem Ipsum is simply dummy text.</span></div>
  <div class="u-item" style="left:624px;top:272px"><svg width="16" height="16"><path d="M1 1l14 7-14 7 4-7z" fill="#fbc33b"/></svg><span style="margin-left:8px">Lorem Ipsum is simply dummy text.</span></div>
  <div class="u-item" style="left:624px;top:308px"><svg width="16" height="16"><path d="M1 1l14 7-14 7 4-7z" fill="#fbc33b"/></svg><span style="margin-left:8px">Lorem Ipsum is simply dummy text.</span></div>
  <div class="u-item" style="left:624px;top:349px"><svg width="16" height="16"><path d="M1 1l14 7-14 7 4-7z" fill="#fbc33b"/></svg><span style="margin-left:8px">Lorem Ipsum is simply dummy text.</span></div>
  <div class="u-item" style="left:624px;top:385px"><svg width="16" height="16"><path d="M1 1l14 7-14 7 4-7z" fill="#fbc33b"/></svg><span style="margin-left:8px">Lorem Ipsum is simply dummy text.</span></div>
  <div class="u-item" style="left:624px;top:425px"><svg width="16" height="16"><path d="M1 1l14 7-14 7 4-7z" fill="#fbc33b"/></svg><span style="margin-left:8px">Lorem Ipsum is simply dummy text.</span></div>
</section>

<section>
  <h2 class="section-title" style="top:2168px">Emergency trade list</h2>
  <p class="section-sub" style="top:2223px">Lorem Ipsum is simply dummy text of the printing and typesetting industry. Lorem Ipsum has been the industry's standard dummy text ever since the 1500s, when an unknown printer.</p>
  <div class="abs filter">Filter By <span class="caret"></span></div>
  <div class="abs trade" style="left:59px"><h3>Company<br>Name</h3><div class="trade-desc">Lorem Ipsum</div><div class="trade-phone">123 456 7890</div></div>
  <div class="abs trade" style="left:430px"><h3>Company<br>Name</h3><div class="trade-desc">Lorem Ipsum</div><div class="trade-phone">123 456 7890</div></div>
  <div class="abs trade" style="left:800px"><h3>Company<br>Name</h3><div class="trade-desc">Lorem Ipsum</div><div class="trade-phone">123 456 7890</div></div>
</section>

<section>
  <div class="abs tenancy"></div>
  <h2 class="section-title" style="top:2768px">End of your tenancy</h2>
  <p class="section-sub" style="top:2828px;left:280px;width:640px;font-size:13.5px">Lorem Ipsum is simply dummy text of the printing and typesetting industry. Lorem Ipsum has been the industry's standard dummy text ever since the 1500s, when an unknown printer took a galley of type and scrambled it to make a type specimen book. It has survived not only five centuries, but also the leap into electronic typesetting, remaining essentially unchanged.</p>
  <p class="section-sub" style="top:2931px;left:280px;width:640px;font-size:13.5px">It was popularised in the 1960s with the release of Typeline sheets containing Lorem Ipsum passages, and more recently with desktop publishing software like Pagecraft Studio including versions of Lorem Ipsum.</p>
</section>

<footer>
  <div class="abs footer-logo"><span class="logo-dot"></span><span class="logo-name" style="font-size:26px">Brindlewood</span></div>
  <p class="abs footer-about">Lorem ipsum dolor sit amet, consectetur adipiscing elit, sed do eiusmod tempor...</p>
  <div class="abs f-head" style="left:332px;top:3090px">Site Map</div>
  <ul class="abs f-links" style="list-style:none">
    <li>Home</li><li>About Us</li><li>Landload</li><li>Tenant</li><li>Make a Switch</li><li>Property Sales</li><li>Appraisal now</li>
  </ul>
  <div class="abs f-contact">
    <div class="f-head">Contact Us</div>
    <div class="f-row"><svg width="18" height="22" fill="none" stroke="#444" stroke-width="1.3"><path d="M9 20S2 12 2 8a7 7 0 0114 0c0 4-7 12-7 12z"/><circle cx="9" cy="8" r="2.5"/></svg><span>18 Kestrel Lane,<br>Harwood, ACT, 2900</span></div>
    <div class="f-row"><svg width="18" height="18" fill="none" stroke="#444" stroke-width="1.3"><path d="M3 1h4l2 5-3 2a11 11 0 005 5l2-3 5 2v4a2 2 0 01-2 2A16 16 0 011 3a2 2 0 012-2z"/></svg><span style="font-weight:600">02 5550 1234<br><span style="display:inline-block;margin-top:4px">02 5550 5678</span></span></div>
    <div class="f-row"><svg width="20" height="16" fill="none" stroke="#444" stroke-width="1.3"><rect x="1" y="1" width="18" height="14"/><path d="M1 1l9 7 9-7"/></svg><span>info@brindlewoodhomes.com.au</span></div>
  </div>
  <div class="abs f-social">
    <div class="f-head">Social Media</div>
    <div class="soc"><span class="fill"></span><span></span><span></span><span></span></div>
  </div>
  <div class="abs bottom">
    <span>2022© Brindlewood Properties. All right reserved.</span>
    <nav><span>Privacy</span><span>Complaint Handling &amp; Dispute Resolution</span><span>Due Diligence Checklist</span></nav>
  </div>
</footer>

</body>
</html>
```